Create a beautiful brochure for a Permanent Make Up Clinic

I need a classy brochure for my Permanent Make up Clinic. It needs a classy cover and the list of services and extra information on the inside. I don't have any requirements on size of the brochure, but it needs to look attractive and upmarket. The colors I like are black -white - Gold - grey. I like a minimalistic look.
I’d like to have my logo on the cover, the price list on the inside and the address information at the back.

Target Market(s)

woman between 18 and 99 years old

Industry/Entity Type

Beauty

Font styles to use
Sans Serif
Script

Colors

Designer to choose colors to be used in the design.

Requirements
Must have
• the logo on the cover
• pictures of the services with an explanation and pricing
• address information at the back
Nice to have
• a classy upmarket look, not with too many different colors in it.

```html
<!DOCTYPE html>
<html lang="en">
<head>
<meta charset="utf-8">
<title>Velora Clinic – Permanent Make Up Brochure</title>
<link href="https://fonts.googleapis.com/css2?family=Montserrat:wght@300;400;600&display=swap" rel="stylesheet">
<style>
  :root{
    --bg:#ececec;
    --paper:#ffffff;
    --slate:#5e5f63;
    --slate-dark:#4d4e52;
    --rose:#d8a496;
    --ink:#3d3d40;
    --muted:#8a8b8f;
    --skin-a:#efe1d8;
    --skin-b:#d9bcab;
    --mono-a:#d6d6d6;
    --mono-b:#8f8f8f;
  }
  *{box-sizing:border-box;margin:0;padding:0}
  html,body{width:1200px;height:2392px;overflow:hidden;background:var(--bg);font-family:'Montserrat',sans-serif;color:var(--ink)}
  .spread{position:absolute;left:30px;width:1140px;height:1130px;display:flex;box-shadow:0 6px 24px rgba(0,0,0,.12)}
  .spread--outside{top:40px}
  .spread--inside{top:1222px}
  .panel{position:relative;width:380px;height:1130px;background:var(--paper);overflow:hidden}
  .panel + .panel{border-left:1px solid #e3e3e3}
  .photo{position:absolute}
  .photo--skin{background:linear-gradient(160deg,var(--skin-a),var(--skin-b))}
  .photo--mono{background:linear-gradient(150deg,var(--mono-a),var(--mono-b))}
  .curve{position:absolute;left:0;width:380px}
  .brand{position:absolute;left:0;width:100%;text-align:center;color:var(--ink);font-weight:400}
  .brand__name{font-size:34px;letter-spacing:2px}
  .brand__sub{font-size:11px;letter-spacing:6px;text-transform:uppercase;margin-top:4px}
  .title{font-weight:300;text-transform:uppercase;letter-spacing:3px}
  .on-slate{color:#fff}
  .copy{font-size:12px;line-height:1.75;font-weight:300}
  .heading{font-size:14px;font-weight:600;letter-spacing:2px;text-transform:uppercase;margin-bottom:10px}
  .rule{height:1px;background:var(--rose);width:60px;margin:14px 0}
  .block{position:absolute;left:36px;right:36px}
  .price-list{list-style:none;font-size:12px;font-weight:300}
  .price-list li{display:flex;justify-content:space-between;padding:7px 0;border-bottom:1px solid rgba(255,255,255,.25)}
  .price-list--dark li{border-bottom-color:#ddd}
  .contact{list-style:none;font-size:12px;line-height:1.9;text-align:center}
  .social{display:flex;justify-content:center;gap:12px;margin-top:14px}
  .social span{width:22px;height:22px;border-radius:50%;background:var(--slate)}
  .web{position:absolute;bottom:38px;width:100%;text-align:center;font-size:11px;letter-spacing:3px}
</style>
</head>
<body>

<!-- OUTSIDE: flap | back | cover -->
<section class="spread spread--outside">
  <article class="panel panel--flap">
    <div class="block" style="top:70px">
      <h2 class="heading">What is permanent make up?</h2>
      <div class="rule"></div>
      <p class="copy">Permanent make up is a gentle cosmetic treatment that places fine pigment in the skin to enhance brows, lips and eyes. Results look soft and natural and last for years.</p>
      <p class="copy" style="margin-top:14px">Wake up ready every morning, save time and feel confident in any weather, at the gym or on holiday.</p>
    </div>
    <svg class="curve" style="top:560px" width="380" height="570" viewBox="0 0 380 570">
      <path d="M0 60 Q190 0 380 40 L380 570 L0 570Z" fill="var(--slate)"/>
      <path d="M0 46 Q190 -14 380 26" fill="none" stroke="var(--rose)" stroke-width="2"/>
    </svg>
    <div class="photo photo--mono" role="img" aria-label="Photo of permanent make up tools and pigments" style="left:36px;right:36px;top:650px;height:260px"></div>
    <div class="block on-slate" style="top:940px">
      <p class="copy">Every treatment starts with a personal consultation and a carefully drawn design.</p>
    </div>
  </article>

  <article class="panel panel--back">
    <div class="brand" style="top:90px">
      <div class="brand__name">Velora</div>
      <div class="brand__sub">Clinic</div>
    </div>
    <div class="photo photo--skin" role="img" aria-label="Portrait photo of a client" style="left:125px;top:220px;width:130px;height:130px;border-radius:50%;border:3px solid var(--rose)"></div>
    <div class="block" style="top:400px">
      <ul class="contact">
        <li>Velora Clinic</li>
        <li>12 Linden Avenue</li>
        <li>1000 AB Brookhaven</li>
        <li>+31 20 555 0148</li>
        <li>hello@veloraclinic.com</li>
      </ul>
      <div class="social"><span></span><span></span><span></span></div>
    </div>
    <svg class="curve" style="top:820px" width="380" height="310" viewBox="0 0 380 310">
      <path d="M0 50 Q190 0 380 40 L380 310 L0 310Z" fill="var(--slate)"/>
      <path d="M0 36 Q190 -14 380 26" fill="none" stroke="var(--rose)" stroke-width="2"/>
    </svg>
    <div class="web on-slate">www.veloraclinic.com</div>
  </article>

  <article class="panel panel--cover">
    <div class="photo photo--skin" role="img" aria-label="Beauty portrait photo of a woman with flawless make up" style="left:0;top:0;width:380px;height:780px"></div>
    <div class="brand" style="top:50px">
      <div class="brand__name">Velora</div>
      <div class="brand__sub">Clinic</div>
    </div>
    <svg class="curve" style="top:700px" width="380" height="430" viewBox="0 0 380 430">
      <path d="M0 60 Q190 0 380 40 L380 430 L0 430Z" fill="var(--slate)"/>
      <path d="M0 44 Q190 -16 380 24" fill="none" stroke="var(--rose)" stroke-width="2"/>
    </svg>
    <div class="block on-slate" style="top:820px;text-align:center">
      <h1 class="title" style="font-size:26px">Permanent Make Up</h1>
      <p class="copy" style="margin-top:8px">Natural beauty, every single day</p>
    </div>
    <div class="web on-slate">www.veloraclinic.com</div>
  </article>
</section>

<!-- INSIDE: three panels -->
<section class="spread spread--inside">
  <article class="panel" style="background:var(--slate)">
    <div class="block on-slate" style="top:70px">
      <h2 class="heading">Eyebrows</h2>
      <div class="rule"></div>
      <p class="copy">Soft hair strokes or a powder finish give fuller, balanced brows shaped to suit your face.</p>
      <ul class="price-list" style="margin-top:16px">
        <li><span>Hair stroke brows</span><span>€ 350</span></li>
        <li><span>Powder brows</span><span>€ 375</span></li>
        <li><span>Touch up</span><span>€ 120</span></li>
      </ul>
    </div>
    <svg class="curve" style="top:640px" width="380" height="490" viewBox="0 0 380 490">
      <path d="M0 40 Q190 0 380 50 L380 490 L0 490Z" fill="var(--paper)"/>
      <path d="M0 26 Q190 -14 380 36" fill="none" stroke="var(--rose)" stroke-width="2"/>
    </svg>
    <div class="photo photo--skin" role="img" aria-label="Photo of a smiling woman touching her face" style="left:0;top:700px;width:380px;height:430px"></div>
  </article>

  <article class="panel">
    <div class="brand" style="top:50px">
      <div class="brand__name" style="font-size:28px">Velora</div>
      <div class="brand__sub">Clinic</div>
    </div>
    <div class="block" style="top:170px">
      <h2 class="heading">Lips</h2>
      <div class="rule"></div>
      <p class="copy">Lip blush adds definition and a fresh tint for lips that look naturally full.</p>
      <ul class="price-list price-list--dark" style="margin-top:12px">
        <li><span>Lip blush</span><span>€ 395</span></li>
        <li><span>Lip contour</span><span>€ 325</span></li>
      </ul>
    </div>
    <div class="photo photo--mono" role="img" aria-label="Photo of a brow treatment in progress" style="left:0;top:500px;width:380px;height:250px"></div>
    <div class="block" style="top:790px">
      <h2 class="heading">Aftercare</h2>
      <div class="rule"></div>
      <p class="copy">Keep the area clean and dry, avoid sun and sauna for two weeks and book your free check after six weeks.</p>
    </div>
  </article>

  <article class="panel" style="background:var(--slate)">
    <div class="photo photo--skin" role="img" aria-label="Close-up photo of an eye with eyeliner" style="left:0;top:0;width:380px;height:420px"></div>
    <svg class="curve" style="top:380px" width="380" height="80" viewBox="0 0 380 80">
      <path d="M0 50 Q190 0 380 30 L380 80 L0 80Z" fill="var(--slate)"/>
      <path d="M0 36 Q190 -14 380 16" fill="none" stroke="var(--rose)" stroke-width="2"/>
    </svg>
    <div class="block on-slate" style="top:500px">
      <h2 class="heading">Eyeliner</h2>
      <div class="rule"></div>
      <p class="copy">A fine lash line or a soft wing opens the eyes and frames your look without smudging.</p>
      <ul class="price-list" style="margin-top:16px">
        <li><span>Lash line</span><span>€ 250</span></li>
        <li><span>Classic eyeliner</span><span>€ 295</span></li>
        <li><span>Consultation</span><span>Free</span></li>
      </ul>
    </div>
  </article>
</section>

</body>
</html>
```